Postcard Design

A house cleaning business. Focus on time saving and stress free. Free estimates. Want it to state that we can make your home sparkle or shine. I have been using the colors purple and black in the logo which I will attach.

Reason: I need a few more days to decide on this. Thank you

Industry/Entity Type

House

Colors
886aae
6b449b

Requirements
Must have
• website www.marlowbrookcare.us
phone # 607-391-2858

```html
<!DOCTYPE html>
<html lang="en">
<head>
<meta charset="utf-8">
<title>Marlow Brook Cleaning Company Postcard</title>
<link href="https://fonts.googleapis.com/css2?family=Playball&family=Cabin:wght@400;500&family=Roboto+Condensed:wght@400&display=swap" rel="stylesheet">
<style>
  :root {
    --purple-deep: #5a2a7e;
    --purple-mid: #6b449b;
    --purple-soft: #886aae;
    --badge-purple: #6a3c8c;
    --ink: #111111;
    --white: #ffffff;
    --frame: #141414;
  }
  * { margin: 0; padding: 0; box-sizing: border-box; }
  html, body { width: 1200px; height: 924px; overflow: hidden; background: var(--white); }
  .postcard {
    position: relative;
    width: 1200px;
    height: 924px;
    overflow: hidden;
    background: var(--white);
    font-family: "Cabin", "Candara", sans-serif;
    color: var(--ink);
  }
  .hero-band {
    position: absolute;
    left: 0; top: 0;
    width: 1200px; height: 478px;
    background: linear-gradient(180deg, #120914 0%, #3a1850 14%, var(--purple-deep) 30%, #5b2a7f 50%, #3b1a52 72%, #0d070f 100%);
  }
  .headline {
    position: absolute;
    left: 0; top: 40px; width: 1200px;
    text-align: center;
    font-family: "Playball", cursive;
    font-size: 74px;
    color: var(--white);
    letter-spacing: 1px;
  }
  .intro {
    position: absolute;
    left: 0; top: 180px; width: 1200px;
    text-align: center;
    color: var(--white);
    font-size: 38px;
    line-height: 52px;
  }
  .assurance {
    position: absolute;
    left: 0; top: 290px; width: 1200px;
    text-align: center;
    color: var(--white);
    font-size: 50px;
    letter-spacing: 0.5px;
  }
  .room-frame {
    position: absolute;
    top: 400px;
    width: 246px; height: 168px;
    background: var(--white);
    border: 5px solid var(--frame);
    padding: 7px;
    box-shadow: 0 2px 6px rgba(0,0,0,0.35);
  }
  .room-frame .room-photo { width: 100%; height: 100%; }
  .room-kitchen { left: 50px; }
  .room-bath { left: 336px; }
  .room-window { left: 621px; }
  .room-lounge { left: 906px; }
  .room-kitchen .room-photo { background: linear-gradient(160deg, #e9eef0 0%, #b7d93a 45%, #8fbf1e 65%, #6a3a22 100%); }
  .room-bath .room-photo { background: linear-gradient(170deg, #6c5a4c 0%, #d9dcd6 35%, #b8c4bd 60%, #e8ebe6 100%); }
  .room-window .room-photo { background: linear-gradient(100deg, #9bc43a 0%, #c8dd8a 22%, #eef0ee 45%, #e3e5e3 100%); }
  .room-lounge .room-photo { background: linear-gradient(170deg, #d6c79a 0%, #e9e9e4 40%, #b8d84c 60%, #e4d9bf 100%); }

  .estimate-badge { position: absolute; left: 66px; top: 594px; width: 224px; height: 224px; }
  .estimate-text {
    position: absolute;
    left: 66px; top: 594px; width: 224px; height: 224px;
    display: flex; align-items: center; justify-content: center;
    text-align: center;
    font-family: "Playball", cursive;
    font-size: 46px;
    line-height: 52px;
    color: var(--white);
    transform: rotate(62deg);
  }
  .phone {
    position: absolute;
    left: 84px; top: 832px;
    font-family: "Roboto Condensed", "Arial Narrow", sans-serif;
    font-size: 40px;
    color: var(--ink);
  }
  .service-list {
    position: absolute;
    left: 334px; top: 636px;
    width: 560px;
    list-style: none;
    display: grid;
    grid-template-columns: 188px 193px 170px;
    row-gap: 8px;
    font-size: 26px;
  }
  .service-list li { display: flex; align-items: center; gap: 6px; height: 32px; }
  .service-list svg { width: 20px; height: 20px; flex: none; }
  .contact-lines {
    position: absolute;
    left: 443px; top: 808px;
    font-size: 25px;
    line-height: 34px;
    letter-spacing: 0.3px;
  }
  .brand-mark {
    position: absolute;
    left: 905px; top: 610px; width: 250px; height: 190px;
    display: flex; flex-direction: column; align-items: center; justify-content: center; gap: 14px;
  }
  .brand-dot { width: 70px; height: 70px; border-radius: 50%; background: var(--purple-soft); }
  .brand-name {
    font-family: "Cabin", "Candara", sans-serif;
    font-size: 32px;
    font-weight: 500;
    color: var(--purple-mid);
    text-align: center;
    line-height: 36px;
  }
  .tagline {
    position: absolute;
    left: 900px; top: 824px; width: 262px;
    text-align: center;
    font-family: "Playball", cursive;
    font-size: 25px;
    line-height: 29px;
    color: var(--ink);
  }
</style>
</head>
<body>
<main class="postcard">
  <div class="hero-band"></div>
  <h1 class="headline">A sparking shine, Every time</h1>
  <p class="intro">Marlow Brook cleaning company offers old fashion,<br>high-quality home cleaning services</p>
  <p class="assurance">Our professionals are insured and bonded</p>

  <div class="room-frame room-kitchen"><div class="room-photo" role="img" aria-label="Photo of a bright green modern kitchen"></div></div>
  <div class="room-frame room-bath"><div class="room-photo" role="img" aria-label="Photo of a clean spacious bathroom with a tub"></div></div>
  <div class="room-frame room-window"><div class="room-photo" role="img" aria-label="Photo of a bright window with green curtains and a plant"></div></div>
  <div class="room-frame room-lounge"><div class="room-photo" role="img" aria-label="Photo of a living room with a white sofa and shiny floor"></div></div>

  <svg class="estimate-badge" viewBox="0 0 224 224" aria-hidden="true">
    <circle cx="112" cy="112" r="112" fill="var(--badge-purple)"/>
    <circle cx="112" cy="112" r="98" fill="none" stroke="var(--white)" stroke-width="2.5" stroke-dasharray="10 7"/>
  </svg>
  <div class="estimate-text">Free<br>Estimate!</div>
  <p class="phone">607-391-2858</p>

  <ul class="service-list">
    <li><svg viewBox="0 0 20 20"><path d="M3 11 L8 16 L17 3" fill="none" stroke="#111" stroke-width="3"/></svg>Kitchens</li>
    <li><svg viewBox="0 0 20 20"><path d="M3 11 L8 16 L17 3" fill="none" stroke="#111" stroke-width="3"/></svg>Baseboards</li>
    <li><svg viewBox="0 0 20 20"><path d="M3 11 L8 16 L17 3" fill="none" stroke="#111" stroke-width="3"/></svg>Bathroom</li>
    <li><svg viewBox="0 0 20 20"><path d="M3 11 L8 16 L17 3" fill="none" stroke="#111" stroke-width="3"/></svg>Scrubbing</li>
    <li><svg viewBox="0 0 20 20"><path d="M3 11 L8 16 L17 3" fill="none" stroke="#111" stroke-width="3"/></svg>Sweeping</li>
    <li><svg viewBox="0 0 20 20"><path d="M3 11 L8 16 L17 3" fill="none" stroke="#111" stroke-width="3"/></svg>Dusting</li>
    <li><svg viewBox="0 0 20 20"><path d="M3 11 L8 16 L17 3" fill="none" stroke="#111" stroke-width="3"/></svg>Vaccuming</li>
    <li><svg viewBox="0 0 20 20"><path d="M3 11 L8 16 L17 3" fill="none" stroke="#111" stroke-width="3"/></svg>Mopping</li>
    <li><svg viewBox="0 0 20 20"><path d="M3 11 L8 16 L17 3" fill="none" stroke="#111" stroke-width="3"/></svg>Appliances</li>
  </ul>

  <p class="contact-lines">www.marlowbrookcare.us<br>marlowbrook33@mailbox.com</p>

  <div class="brand-mark">
    <span class="brand-dot"></span>
    <span class="brand-name">Marlow Brook<br>Cleaning Company</span>
  </div>
  <p class="tagline">We can make your<br>house sparkle!</p>
</main>
</body>
</html>
```